Kestrel Flooring Supply

Basic one-sided business card design using the attached logo. Vintage americana theme. Font is modified Arial Nova Cond, but anything that coordinates can be used

```html
<!DOCTYPE html>
<html lang="en">
<head>
<meta charset="utf-8">
<title>Kestrel Flooring Supply — Business Card</title>
<link href="https://fonts.googleapis.com/css2?family=Oswald:wght@600&family=Arimo:wght@400;700&display=swap" rel="stylesheet">
<style>
  :root {
    --backdrop: #1c1d1f;
    --card-dark: #2b2b2c;
    --card-light: #fbfbfb;
    --gold: #b8926a;
    --ink: #2a2a2a;
    --white: #ffffff;
  }
  * { box-sizing: border-box; margin: 0; padding: 0; }
  html, body {
    width: 1200px; height: 840px; overflow: hidden;
    background: var(--backdrop);
  }
  .canvas {
    position: relative; width: 1200px; height: 840px;
  }
  .card {
    position: absolute; left: 320px;
    width: 560px; height: 320px;
    border-radius: 22px;
    overflow: hidden;
    box-shadow: 0 0 0 2px var(--gold), 0 14px 30px rgba(0,0,0,.5);
  }
  .card--front { top: 70px; background: var(--card-dark); }
  .card--back  { top: 450px; background: var(--card-light); }

  .brand-name {
    font-family: "Oswald", "Arial Narrow", sans-serif;
    font-weight: 600;
    color: var(--white);
    text-transform: uppercase;
    text-align: center;
    line-height: 1.05;
  }
  .card--front .brand-name {
    position: absolute; inset: 0;
    display: flex; align-items: center; justify-content: center;
    padding: 0 40px;
    font-size: 40px; letter-spacing: 1px;
  }

  .back-disc {
    position: absolute;
    left: 300px; top: -110px;
    width: 380px; height: 380px;
    border-radius: 50%;
    background: var(--card-dark);
  }
  .back-disc::after {
    content: "";
    position: absolute; inset: 14px;
    border-radius: 50%;
    border: 3px solid var(--gold);
  }
  .card--back .brand-name {
    position: absolute;
    left: 340px; top: 40px; width: 200px; height: 160px;
    display: flex; align-items: center; justify-content: center;
    font-size: 30px; letter-spacing: .5px;
  }

  .contact {
    position: absolute; left: 40px; top: 92px;
    font-family: "Arimo", Arial, sans-serif;
    color: var(--ink);
  }
  .contact__name {
    font-weight: 700; font-size: 21px; color: var(--gold);
    text-transform: uppercase; letter-spacing: .3px;
  }
  .contact__role { font-size: 14px; margin-top: 2px; }
  .contact__address { font-size: 14px; line-height: 1.35; margin-top: 26px; padding-left: 30px; }
  .contact__list { list-style: none; margin-top: 26px; padding-left: 30px; font-size: 14px; }
  .contact__list li { display: flex; align-items: center; gap: 8px; line-height: 1.7; }
  .contact__list svg { width: 14px; height: 14px; flex: none; }
</style>
</head>
<body>
<main class="canvas">
  <section class="card card--front">
    <p class="brand-name">Kestrel Flooring Supply</p>
  </section>

  <section class="card card--back">
    <div class="back-disc"></div>
    <p class="brand-name">Kestrel<br>Flooring Supply</p>

    <div class="contact">
      <p class="contact__name">Daniel Whitaker</p>
      <p class="contact__role">Manager</p>
      <p class="contact__address">Your Address, City<br>State, Zip 0000</p>
      <ul class="contact__list">
        <li>
          <svg viewBox="0 0 16 16" aria-hidden="true"><path d="M4 1.5l2.2 3-1.4 1.6a8 8 0 0 0 5 5l1.6-1.4 3 2.2-1.2 2.4C7.5 14.6 1.4 8.5 1.6 2.7z" fill="none" stroke="var(--gold)" stroke-width="1.4" stroke-linejoin="round"/></svg>
          321-555-0187
        </li>
        <li>
          <svg viewBox="0 0 16 16" aria-hidden="true"><rect x="1.5" y="3.5" width="13" height="9" fill="none" stroke="var(--gold)" stroke-width="1.4"/><path d="M1.5 3.5l6.5 5 6.5-5" fill="none" stroke="var(--gold)" stroke-width="1.4"/></svg>
          youremail@kestrelmail.com
        </li>
        <li>
          <svg viewBox="0 0 16 16" aria-hidden="true"><g fill="none" stroke="var(--gold)" stroke-width="1.3"><circle cx="8" cy="8" r="6.5"/><ellipse cx="8" cy="8" rx="3" ry="6.5"/><path d="M1.5 8h13M2.5 4.8h11M2.5 11.2h11"/></g></svg>
          www.yourwebsite.com
        </li>
      </ul>
    </div>
  </section>
</main>
</body>
</html>
```